App für weniger Konsum
Zielgruppe
Wir sind ein Startup, das Nutzer:innen in einem bewussteren Kaufverhalten stärkt. Dabei werden Nutzer:innen psychologischen Kaufprofilen zugeordnet und individuell auf dem Weg begleitet, weniger einzukaufen. Das stärkt die Finanzen und schützt die Umwelt.
Aufgabenstellung
Das Design sollte einerseits minimalismusorientierte Nutzer:innen ansprechen (clean, ruhig), aber auch Nutzer:innen ansprechen, die sich noch nicht mit weniger / besserem Konsum beschäftigt haben.
Es wäre toll folgende Slides zu haben:
- Anmeldung / Registrierung
- Quiz (Es soll direkt zu Beginn ein Quiz aus mehreren Slides geben, das Nutzer:innen einem Kauftypen zuordnet(
- Quizergebnis (Du bist Kauftyp XYZ...)
- Home-Screen der App / Navigation
- Statistiken: Du hast diesen Monat so viel gespart...
- Slide mit Einstellungen
- 'Challenge' Slide: 10 tage aussortieren

```html
<!DOCTYPE html>
<html lang="de">
<head>
<meta charset="utf-8">
<title>Bewusst – App-Screens</title>
<link href="https://fonts.googleapis.com/css2?family=Manrope:wght@400;500;600;700&display=swap" rel="stylesheet">
<style>
:root{
  --stage:#133224;
  --screen:#f7f6f3;
  --card:#ffffff;
  --green:#62a182;
  --green-dark:#4f8a6d;
  --green-soft:#e6efe9;
  --ink:#1f2a24;
  --muted:#8a918c;
  --line:#e7e6e2;
  --orange:#f0923a;
  --orange-soft:#fdf1e4;
  --pink:#f1dde6;
  --blue:#dfe7f5;
  --red:#e46464;
}
*{box-sizing:border-box;margin:0;padding:0}
html,body{width:751px;height:1200px;overflow:hidden}
body{background:var(--stage);font-family:"Manrope",sans-serif;color:var(--ink);position:relative}
.screen{position:absolute;width:157px;background:var(--screen);overflow:hidden}
.abs{position:absolute}
.title{font-size:9px;font-weight:600}
.sub{font-size:5px;color:var(--muted)}
.btn{position:absolute;left:12px;right:12px;height:20px;border-radius:4px;background:var(--green);color:#fff;font-size:5.5px;font-weight:600;display:flex;align-items:center;justify-content:center;gap:4px}
.card{position:absolute;left:8px;right:8px;background:var(--card);border-radius:5px;box-shadow:0 1px 2px rgba(0,0,0,.04)}
.nav{position:absolute;left:0;right:0;bottom:0;height:32px;background:#fff;border-top:1px solid var(--line);display:flex;justify-content:space-around;align-items:center;padding:0 4px}
.nav span{display:flex;flex-direction:column;align-items:center;gap:2px;font-size:3px;font-weight:600;color:var(--muted);letter-spacing:.2px}
.nav span.on{color:var(--green)}
.nav svg{width:7px;height:7px;stroke:currentColor;fill:none;stroke-width:2}
.label{font-size:5px;font-weight:600}
.input{position:absolute;left:12px;right:12px;height:20px;border:1px solid var(--line);border-radius:4px;background:#fff;font-size:5px;padding-left:7px;display:flex;align-items:center}
.option{position:absolute;left:11px;right:11px;height:24px;background:#fff;border:1px solid var(--line);border-radius:4px;font-size:6px;padding:0 7px;display:flex;align-items:center;justify-content:space-between}
.radio{width:6px;height:6px;border:1px solid var(--line);border-radius:50%}
.item{position:absolute;left:8px;right:8px;height:31px;background:#fff;border-radius:4px;padding:0 7px;display:flex;justify-content:space-between;align-items:center}
.item b{font-size:5.8px;font-weight:600;display:block}
.item i{font-style:normal;font-size:3.8px;color:var(--muted)}
.item .p{text-align:right;font-size:5.5px;font-weight:600}
.item .p em{display:block;font-style:normal;font-size:3px;color:var(--green);letter-spacing:.3px;margin-top:3px}
.task{position:absolute;left:8px;right:8px;height:26px;background:#fff;border-radius:4px;display:flex;align-items:center;gap:6px;padding-left:6px}
.task.done{background:#eef1ef;border:1px solid #dfe3e0}
.task .n{width:10px;height:10px;border-radius:50%;background:#f0efec;font-size:3.5px;color:var(--muted);display:flex;align-items:center;justify-content:center}
.task.done .n{background:var(--green);color:#fff}
.task b{font-size:5.5px;font-weight:500;display:block}
.task.done b{text-decoration:line-through;color:var(--green)}
.task i{font-style:normal;font-size:3.8px;color:var(--muted)}
.row{display:flex;align-items:center;gap:6px;padding:0 8px;height:27px}
.ic{width:12px;height:12px;border-radius:50%;display:flex;align-items:center;justify-content:center}
.ic svg{width:6px;height:6px;fill:none;stroke-width:2}
.cap{font-size:4.5px;font-weight:600;color:var(--muted);letter-spacing:.5px}
.placeholder{position:absolute;border-radius:6px}
</style>
</head>
<body>
<svg width="0" height="0" style="position:absolute">
  <defs>
    <symbol id="i-home" viewBox="0 0 24 24"><path d="M3 10l9-7 9 7v10a1 1 0 0 1-1 1h-5v-7H9v7H4a1 1 0 0 1-1-1z"/></symbol>
    <symbol id="i-box" viewBox="0 0 24 24"><path d="M12 2l9 5v10l-9 5-9-5V7z M3 7l9 5 9-5 M12 12v10"/></symbol>
    <symbol id="i-trend" viewBox="0 0 24 24"><path d="M2 17l7-7 4 4 9-9 M15 5h7v7"/></symbol>
    <symbol id="i-cup" viewBox="0 0 24 24"><path d="M7 3h10v7a5 5 0 0 1-10 0z M7 5H3a4 4 0 0 0 4 5 M17 5h4a4 4 0 0 1-4 5 M12 15v4 M8 21h8"/></symbol>
    <symbol id="i-user" viewBox="0 0 24 24"><circle cx="12" cy="8" r="4"/><path d="M4 21a8 8 0 0 1 16 0"/></symbol>
  </defs>
</svg>

<!-- Willkommen -->
<section class="screen" style="left:33px;top:387px;height:324px">
  <div class="placeholder" role="img" aria-label="Illustration: entspannt liegende Person mit Tablet" style="left:24px;top:42px;width:110px;height:68px;background:linear-gradient(135deg,#e7e5e1,#d8c9b4)"></div>
  <div class="abs" style="left:10px;right:10px;top:145px;text-align:center;font-size:10.5px;font-weight:500;line-height:1.25">Entdecke, was dir wirklich guttut.</div>
  <div class="abs sub" style="left:8px;right:8px;top:177px;text-align:center;font-size:6px;line-height:1.6">Lerne deine Konsumgewohnheiten besser kennen – Schritt für Schritt, ohne Druck.</div>
  <div class="btn" style="top:218px">Bist du bereit? <span>→</span></div>
</section>

<!-- Anmeldung -->
<section class="screen" style="left:211px;top:387px;height:324px">
  <div class="abs" style="left:0;right:0;top:30px;text-align:center;font-size:10.5px;font-weight:500">Lasst uns beginnen</div>
  <div class="abs" style="left:19px;top:68px;width:60px;text-align:center;font-size:6.5px;color:var(--green);font-weight:600;border-bottom:1.5px solid var(--green);padding-bottom:2px">Anmelden</div>
  <div class="abs" style="left:86px;top:68px;font-size:6.5px;color:#cfd1cf">Registrieren</div>
  <div class="abs label" style="left:12px;top:104px">E-Mail-Adresse</div>
  <div class="input" style="top:113px">hi@linamoreau.com</div>
  <div class="abs label" style="left:12px;top:139px">Passwort</div>
  <div class="input" style="top:148px;border-color:var(--red);letter-spacing:1px">•••••••••••</div>
  <div class="abs" style="left:12px;top:173px;font-size:4.5px;color:#d9d9d6">Falsches Passwort</div>
  <div class="abs" style="right:12px;top:173px;font-size:5px;color:var(--green);font-weight:600">Passwort vergessen?</div>
  <div class="btn" style="top:185px">Weiter</div>
  <div class="abs" style="left:34px;right:34px;top:219px;border-top:1px solid var(--line)"></div>
  <div class="abs" style="left:0;right:0;top:215px;text-align:center;font-size:4.5px;color:#d2d2cf"><span style="background:var(--screen);padding:0 3px">Or</span></div>
  <div class="input" style="top:235px;justify-content:center;font-weight:500;gap:3px"><span style="width:5px;height:5px;border-radius:50%;background:var(--ink)"></span>Mit Pomo anmelden</div>
  <div class="input" style="top:260px;justify-content:center;font-weight:500;gap:3px"><span style="width:5px;height:5px;border-radius:50%;background:#5a87d8"></span>Mit Searo anmelden</div>
</section>

<!-- Quiz -->
<section class="screen" style="left:388px;top:387px;height:324px">
  <div class="abs" style="left:9px;top:7px;font-size:8px;color:var(--muted)">←</div>
  <div class="abs" style="right:9px;top:7px;font-size:8px;color:var(--muted)">→</div>
  <div class="abs" style="left:8px;top:28px;font-size:4.5px;color:var(--muted)">Frage 2 von 5</div>
  <div class="abs" style="left:8px;right:8px;top:37px;height:2px;background:var(--line);border-radius:1px"><div style="width:40%;height:100%;background:var(--green)"></div></div>
  <div class="abs" style="left:12px;right:12px;top:68px;text-align:center;font-size:8.5px;font-weight:500;line-height:1.35">Welches Gefühl löst meistens deinen Kaufdrang aus?</div>
  <div class="option" style="top:106px">Langeweile<span class="radio"></span></div>
  <div class="option" style="top:136px">Stress<span class="radio"></span></div>
  <div class="option" style="top:166px">Belohnung<span class="radio"></span></div>
  <div class="option" style="top:196px">Inspiration<span class="radio"></span></div>
</section>

<!-- Home -->
<section class="screen" style="left:566px;top:387px;height:324px">
  <div class="abs sub" style="left:8px;top:12px;font-size:4.5px">Mittwoch, 28. Jan</div>
  <div class="abs" style="left:8px;top:21px;font-size:10px;font-weight:600">Guten Morgen, Lina.</div>
  <div class="abs" role="img" aria-label="Profilbild" style="right:9px;top:20px;width:11px;height:11px;border-radius:50%;background:#e0703f"></div>
  <div class="abs" style="left:8px;right:8px;top:42px;height:97px;border-radius:9px;background:var(--green);color:#fff;padding:11px 9px">
    <div style="font-size:4.5px;letter-spacing:.4px;opacity:.85">↗ WÖCHENTLICHER EINBLICK</div>
    <div style="font-size:10px;font-weight:600;line-height:1.2;margin-top:4px">3 bewusste Entscheidungen</div>
    <div style="font-size:5.5px;line-height:1.6;margin-top:3px;opacity:.9">Diese Woche hast du unnötige Ausgaben vermieden.</div>
    <div style="display:inline-block;margin-top:7px;font-size:4.5px;background:rgba(255,255,255,.2);padding:3px 6px;border-radius:6px">42,00 € weniger ausgegeben</div>
  </div>
  <div class="abs label" style="left:8px;top:152px;font-size:6px">Aktives Ziel</div>
  <div class="card" style="top:166px;height:34px;border-left:2px solid var(--orange);overflow:hidden;display:flex">
    <div style="flex:1;padding:8px 0 0 8px"><div style="font-size:6px;font-weight:600">7-Tage Konsum-Pause</div><div style="font-size:4px;color:var(--muted);margin-top:3px">Tag 3 von 7 • Dranbleiben!</div></div>
    <div style="width:33px;background:var(--orange-soft);color:var(--orange);font-size:8px;font-weight:700;display:flex;align-items:center;justify-content:center">42%</div>
  </div>
  <div class="abs label" style="left:8px;top:212px;font-size:6px">Tägliche Reflexion</div>
  <div class="card" style="top:226px;height:61px;background:#f1f0ed;padding:9px">
    <div style="font-size:6.5px;line-height:1.4;width:105px">Wie hast du dich nach deinem letzten Kauf gefühlt?</div>
    <div class="abs" style="right:7px;top:7px;width:24px;height:24px;border-radius:50%;border:1.5px solid #e2e1de"></div>
    <div style="display:flex;gap:4px;margin-top:6px">
      <div role="img" aria-label="Stimmung: gut" style="flex:1;height:18px;background:#fff;border-radius:4px;display:flex;align-items:center;justify-content:center"><span style="width:7px;height:7px;border-radius:50%;background:#f5c040"></span></div>
      <div role="img" aria-label="Stimmung: neutral" style="flex:1;height:18px;background:#fff;border-radius:4px;display:flex;align-items:center;justify-content:center"><span style="width:7px;height:7px;border-radius:50%;background:#f5c040"></span></div>
      <div role="img" aria-label="Stimmung: schlecht" style="flex:1;height:18px;background:#fff;border-radius:4px;display:flex;align-items:center;justify-content:center"><span style="width:7px;height:7px;border-radius:50%;background:#f5c040"></span></div>
    </div>
  </div>
  <nav class="nav">
    <span class="on"><svg><use href="#i-home"/></svg>HOME</span><span><svg><use href="#i-box"/></svg>DINGE</span><span><svg><use href="#i-trend"/></svg>TRENDS</span><span><svg><use href="#i-cup"/></svg>ZIELE</span><span><svg><use href="#i-user"/></svg>PROFIL</span>
  </nav>
</section>

<!-- Meine Dinge -->
<section class="screen" style="left:33px;top:731px;height:337px">
  <div class="abs" style="left:8px;top:18px;font-size:9px;font-weight:600">Meine Dinge</div>
  <div class="abs" style="right:8px;top:17px;width:12px;height:12px;border-radius:50%;background:var(--green);color:#fff;font-size:8px;line-height:12px;text-align:center">+</div>
  <div class="abs" style="left:6px;right:6px;top:40px;display:flex;justify-content:space-between">
    <div style="width:36px;text-align:center"><div style="margin:0 auto;width:22px;height:22px;border-radius:50%;background:var(--pink);color:#e0508a;font-size:9px;line-height:22px">♡</div><div style="font-size:3.5px;font-weight:700;margin-top:4px">WUNSCH</div></div>
    <div style="width:36px;text-align:center"><div style="margin:0 auto;width:20px;height:20px;border-radius:50%;background:var(--blue)"></div><div style="font-size:3.5px;color:var(--muted);margin-top:5px">GEKAUFT</div></div>
    <div style="width:36px;text-align:center"><div style="margin:0 auto;width:20px;height:20px;border-radius:50%;background:var(--green-soft)"></div><div style="font-size:3.5px;color:var(--muted);margin-top:5px">VERZICHTET</div></div>
    <div style="width:36px;text-align:center"><div style="margin:0 auto;width:20px;height:20px;border-radius:50%;background:var(--orange-soft)"></div><div style="font-size:3.5px;color:var(--muted);margin-top:5px">AUSGEMISTET</div></div>
  </div>
  <div class="item" style="top:80px"><div><b>Espressomaschine</b><i>Seit 1 Woche</i></div><div class="p">450,00 €<em>REFLEKTIEREN</em></div></div>
  <div class="item" style="top:119px"><div><b>Noise-Cancelling Kopfhörer</b><i>Vor 2 Tagen</i></div><div class="p">289,00 €<em>REFLEKTIEREN</em></div></div>
  <div class="item" style="top:159px"><div><b>Neuer Bürostuhl</b><i>Seit 5 Tagen</i></div><div class="p">349,00 €<em>REFLEKTIEREN</em></div></div>
  <div class="item" style="top:198px"><div><b>Wochenend-Kurztrip</b><i>Vor 2 Tagen</i></div><div class="p">400,00 €<em>REFLEKTIEREN</em></div></div>
  <div class="item" style="top:238px"><div><b>Smartwatch</b><i>Vor 2 Tagen</i></div><div class="p">199,00 €<em>REFLEKTIEREN</em></div></div>
  <div class="item" style="top:277px"><div><b>Minimalistische Stehlampe</b><i>Vor 2 Tagen</i></div><div class="p">159,00 €<em>REFLEKTIEREN</em></div></div>
  <nav class="nav">
    <span><svg><use href="#i-home"/></svg>HOME</span><span class="on"><svg><use href="#i-box"/></svg>DINGE</span><span><svg><use href="#i-trend"/></svg>TRENDS</span><span><svg><use href="#i-cup"/></svg>ZIELE</span><span><svg><use href="#i-user"/></svg>PROFIL</span>
  </nav>
</section>

<!-- Trends -->
<section class="screen" style="left:212px;top:731px;height:450px">
  <div class="abs" style="left:8px;top:17px;font-size:9px;font-weight:600">Bewusstseins-Trends</div>
  <div class="abs sub" style="left:8px;top:32px;font-size:5.5px">Deine psychologische Entwicklung.</div>
  <div class="abs" style="left:8px;right:8px;top:50px;height:48px;border-radius:9px;background:var(--green);color:#fff;padding:8px">
    <div style="font-size:4px;letter-spacing:.5px;opacity:.85">✦ FOKUS SCORE</div>
    <div style="font-size:12px;font-weight:700;margin-top:2px">+85%</div>
    <div style="font-size:4.5px;opacity:.9;margin-top:2px">Deine Impulskontrolle steigt stetig an.</div>
  </div>
  <div class="card" style="top:110px;right:81px;height:55px;text-align:center;padding-top:13px">
    <div class="cap" style="font-size:4px">GESPART</div><div style="font-size:11px;font-weight:600;color:var(--green);margin-top:2px">420€</div><div style="font-size:3.5px;color:#b8d3c5">Diesen Monat</div>
  </div>
  <div class="card" style="top:110px;left:81px;height:55px;text-align:center;padding-top:13px">
    <div class="cap" style="font-size:4px">MINDFUL</div><div style="font-size:11px;font-weight:600;color:var(--orange);margin-top:2px">12</div><div style="font-size:3.5px;color:#f5c08f">Kaufmomente</div>
  </div>
  <div class="card" style="top:176px;height:112px;padding:9px">
    <div style="font-size:6px;font-weight:600">Psychologie &amp; Fokus</div>
    <div class="sub" style="font-size:4.5px;margin-top:3px">Mentale Stärke im Zeitverlauf</div>
    <svg class="abs" style="left:8px;top:38px" width="125" height="60" viewBox="0 0 125 60">
      <defs><linearGradient id="fillg" x1="0" y1="0" x2="0" y2="1"><stop offset="0" stop-color="#62a182" stop-opacity=".25"/><stop offset="1" stop-color="#62a182" stop-opacity="0"/></linearGradient></defs>
      <path d="M2 45 C20 38 35 28 50 30 S70 40 80 32 S105 10 122 5 V58 H2Z" fill="url(#fillg)"/>
      <path d="M2 45 C20 38 35 28 50 30 S70 40 80 32 S105 10 122 5" fill="none" stroke="#62a182" stroke-width="1.5"/>
    </svg>
    <div class="abs" style="left:10px;right:10px;bottom:6px;display:flex;justify-content:space-between;font-size:4px;color:var(--muted)"><span>Di</span><span>Mi</span><span>Do</span><span>Fr</span><span>Sa</span><span>So</span></div>
  </div>
  <div class="abs label" style="left:8px;top:303px;font-size:6px">Erfolge</div>
  <div class="card" style="top:318px;height:28px;display:flex;align-items:center;gap:6px;padding-left:6px"><span class="ic" style="background:var(--blue)"></span><div><div style="font-size:4.8px;font-weight:600">Ruhepol</div><div style="font-size:3.5px;color:var(--muted)">3 Tage ohne Impulskauf</div></div></div>
  <div class="card" style="top:351px;height:28px;display:flex;align-items:center;gap:6px;padding-left:6px"><span class="ic" style="background:#fbf1d8;color:#e8b830;font-size:7px">☆</span><div><div style="font-size:4.8px;font-weight:600">Meister</div><div style="font-size:3.5px;color:var(--muted)">10 Dinge ausgemistet</div></div></div>
  <div class="card" style="top:384px;height:28px;display:flex;align-items:center;gap:6px;padding-left:6px"><span class="ic" style="background:var(--green-soft)"></span><div><div style="font-size:4.8px;font-weight:600">Bewusst</div><div style="font-size:3.5px;color:var(--muted)">Quiz abgeschlossen</div></div></div>
  <nav class="nav">
    <span><svg><use href="#i-home"/></svg>HOME</span><span><svg><use href="#i-box"/></svg>DINGE</span><span class="on"><svg><use href="#i-trend"/></svg>TRENDS</span><span><svg><use href="#i-cup"/></svg>ZIELE</span><span><svg><use href="#i-user"/></svg>PROFIL</span>
  </nav>
</section>

<!-- Challenge -->
<section class="screen" style="left:388px;top:731px;height:427px">
  <div class="abs" style="left:0;right:0;top:0;height:78px;background:var(--green);border-radius:0 0 10px 10px;color:#fff;padding:11px 11px">
    <div style="font-size:9.5px;font-weight:600">10 Tage Ausmisten</div>
    <div style="font-size:5.5px;opacity:.9;margin-top:4px">Platz schafft Klarheit.</div>
    <div style="display:flex;align-items:center;gap:6px;margin-top:9px"><span style="font-size:11px;font-weight:700">20%</span><span style="flex:1;height:2px;background:rgba(255,255,255,.3);border-radius:1px"><span style="display:block;width:20%;height:100%;background:#fff"></span></span></div>
  </div>
  <div class="task done" style="top:86px"><span class="n">✓</span><div><b>Tag 1</b><i>Schreibtisch aufräumen</i></div></div>
  <div class="task done" style="top:118px"><span class="n">✓</span><div><b>Tag 2</b><i>Kleiderschrank checken</i></div></div>
  <div class="task" style="top:149px"><span class="n">3</span><div><b>Tag 3</b><i>Eine Sache spenden</i></div></div>
  <div class="task" style="top:181px"><span class="n">4</span><div><b>Tag 4</b><i>Eine Sache spenden</i></div></div>
  <div class="task" style="top:212px"><span class="n">5</span><div><b>Tag 5</b><i>Eine Sache spenden</i></div></div>
  <div class="task" style="top:244px"><span class="n">6</span><div><b>Tag 6</b><i>Eine Sache spenden</i></div></div>
  <div class="task" style="top:275px"><span class="n">7</span><div><b>Tag 7</b><i>Eine Sache spenden</i></div></div>
  <div class="task" style="top:307px"><span class="n">8</span><div><b>Tag 8</b><i>Eine Sache spenden</i></div></div>
  <div class="task" style="top:338px"><span class="n">9</span><div><b>Tag 9</b><i>Eine Sache spenden</i></div></div>
  <div class="task" style="top:370px"><span class="n">10</span><div><b>Tag 10</b><i>Eine Sache spenden</i></div></div>
  <nav class="nav">
    <span><svg><use href="#i-home"/></svg>HOME</span><span><svg><use href="#i-box"/></svg>DINGE</span><span><svg><use href="#i-trend"/></svg>TRENDS</span><span class="on"><svg><use href="#i-cup"/></svg>ZIELE</span><span><svg><use href="#i-user"/></svg>PROFIL</span>
  </nav>
</section>

<!-- Einstellungen -->
<section class="screen" style="left:565px;top:731px;height:293px">
  <div class="abs" style="left:8px;top:17px;font-size:9px;font-weight:600">Einstellungen</div>
  <div class="abs cap" style="left:10px;top:40px">PRÄFERENZEN</div>
  <div class="card" style="top:55px;height:56px">
    <div class="row"><span class="ic" style="background:#f0efec"></span><div style="flex:1"><div style="font-size:5.5px;font-weight:500">Sanfte Erinnerungen</div><div style="font-size:3.8px;color:var(--muted)">Morgens &amp; Abends</div></div><span style="width:13px;height:7px;border-radius:4px;background:var(--green);position:relative"><span style="position:absolute;right:1px;top:1px;width:5px;height:5px;border-radius:50%;background:#fff"></span></span></div>
    <div class="row"><span class="ic" style="background:var(--orange-soft)"></span><div style="flex:1"><div style="font-size:5.5px;font-weight:500">Erscheinungsbild</div><div style="font-size:3.8px;color:var(--muted)">Hell (Standard)</div></div><span style="font-size:4px;color:var(--muted);background:#f0efec;padding:2px 5px;border-radius:4px">Light</span></div>
  </div>
  <div class="abs cap" style="left:10px;top:123px">MINDFUL TOOLKIT</div>
  <div class="card" style="top:138px;height:56px">
    <div class="row"><span class="ic" style="background:var(--blue)"></span><div style="flex:1;font-size:5.5px;font-weight:500">Impuls-Pause</div><span style="font-size:6px;color:var(--muted)">›</span></div>
    <div class="row"><span class="ic" style="background:var(--pink);color:#e0508a;font-size:6px">♡</span><div style="flex:1;font-size:5.5px;font-weight:500">Freuden-Check</div><span style="font-size:6px;color:var(--muted)">›</span></div>
  </div>
  <div class="card" style="top:205px;height:45px;background:#eff2f0;border:1px solid #e2e7e3;padding:8px 9px">
    <div style="font-size:5.5px;font-weight:600;display:flex;gap:5px;align-items:center"><span style="width:7px;height:7px;border:1px solid var(--green);border-radius:50%"></span>Unsere Philosophie</div>
    <div style="font-size:4.3px;font-style:italic;color:var(--muted);line-height:1.6;margin-top:3px;padding-left:12px">"Bewusster Konsum bedeutet keinen Verzicht – sondern Klarheit darüber, was wirklich zählt."</div>
  </div>
  <nav class="nav">
    <span><svg><use href="#i-home"/></svg>HOME</span><span><svg><use href="#i-box"/></svg>DINGE</span><span><svg><use href="#i-trend"/></svg>TRENDS</span><span><svg><use href="#i-cup"/></svg>ZIELE</span><span class="on"><svg><use href="#i-user"/></svg>PROFIL</span>
  </nav>
</section>
</body>
</html>
```